BrivoMatex. Lantern for the Steady Growth. Business card

Professional business card for BrivoMatex (Lantern for the Steady Growth)
My rationale: Strategy-> Execution-> Results-> Value that lead to the BrivoMatex name: We put the Lantern for the Steady Growth.
We deliver value to our customers helping them at defining a good strategy (cyan arrow). 90% of well formulated strategies fail due to poor execution so we also consider strategical execution very important (green arrow). Due to the execution we obtain the results (blue arrow). Finally, the results provide feedback to redefine strategy, and the new strategy has to be executed and new results obtained providing new feedback and on and on. It's like a wheel that finally, must create corporate value: value for shareholders, staholders, employees, providers...-

Target Market(s)

CEOs and steering comitees , invewrnent funds

Industry/Entity Type

Business Consultant

Contact Information for Business Card

Tommaso Ferlini
CEO & Founder
tommaso.ferlini@brivomatex.example
Mobile: +34 611.205.938
www.brivomatex.example

Colors

Designer to choose colors to be used in the design.

Requirements
Nice to have
• Nice to hace the words: Strategy, execution, results
• Nice to vave the claim: Lantern for the Steady Growth
• The three colors should be shown:
• cyan for STRATEGY
• green for EXECUTION
• blue for RESULTS
Should not have
• Complete black background

```html
<!DOCTYPE html>
<html lang="en">
<head>
<meta charset="utf-8">
<title>BrivoMatex — Business Card</title>
<link rel="stylesheet" href="https://fonts.googleapis.com/css2?family=Source+Sans+3:wght@400;600;700&display=swap">
<style>
  :root{
    --backdrop:#e8ebec;
    --card-white:#ffffff;
    --card-grey:#c9ccce;
    --navy:#283a8e;
    --green:#8cc63f;
    --cyan:#29abe2;
    --pattern-light:#f4f4f4;
    --pattern-grey:#dedfe0;
    --white:#ffffff;
  }
  *{box-sizing:border-box;margin:0;padding:0}
  html,body{width:1200px;height:1200px;overflow:hidden}
  body{background:var(--backdrop);font-family:"Source Sans 3",Arial,sans-serif;position:relative}
  .card{position:absolute;left:354px;width:494px;height:292px}
  .card--back{top:282px;background:var(--card-white)}
  .back-pattern{position:absolute;inset:0;background:linear-gradient(135deg,var(--pattern-light),var(--pattern-grey))}
  .card--front{top:624px;background:var(--card-grey)}
  .brand{position:absolute;left:33px;top:150px;display:flex;align-items:center;gap:10px}
  .brand-dot{width:14px;height:14px;border-radius:50%;background:var(--navy)}
  .brand-name{font-size:33px;font-weight:700;color:var(--navy);letter-spacing:-.5px}
  .pillars{position:absolute;left:33px;top:232px;display:flex;gap:10px;font-size:9px}
  .pillar{display:flex;align-items:center;gap:3px}
  .pillar::before{content:"";width:6px;height:6px;background:var(--white)}
  .pillar--results{color:var(--navy)}
  .pillar--execution{color:var(--green)}
  .pillar--strategy{color:var(--cyan)}
  .person{position:absolute;right:35px;top:46px;text-align:right}
  .person-name{font-size:24px;font-weight:600;color:var(--navy);letter-spacing:.3px}
  .person-role{font-size:11px;color:var(--white);margin-top:6px}
  .contact{position:absolute;right:35px;top:173px;list-style:none;text-align:right;font-size:12px;color:var(--white);line-height:20px}
  .contact li{display:flex;justify-content:flex-end;align-items:center;gap:7px}
  .contact svg{width:9px;height:9px;fill:var(--navy)}
  .tagline{position:absolute;right:40px;top:232px;font-size:9px;color:var(--navy)}
</style>
</head>
<body>
  <section class="card card--back">
    <div class="back-pattern" role="img" aria-label="Repeating pattern of the brand's growth symbol in light grey, one instance in brand colours"></div>
  </section>

  <section class="card card--front">
    <div class="brand">
      <span class="brand-dot"></span>
      <span class="brand-name">BrivoMatex</span>
    </div>
    <div class="pillars">
      <span class="pillar pillar--results">Results</span>
      <span class="pillar pillar--execution">Execution</span>
      <span class="pillar pillar--strategy">Strategy</span>
    </div>

    <div class="person">
      <h1 class="person-name">Tommaso Ferlini</h1>
      <p class="person-role">CEO &amp; Founder</p>
    </div>

    <ul class="contact">
      <li>www.brivomatex.example
        <svg viewBox="0 0 10 10"><path d="M2 0.5l2 2-1 1.3c.6 1.3 1.6 2.3 2.9 2.9l1.3-1 2 2-1.3 1.8C4 9.2.8 6 .2 1.8z"/></svg></li>
      <li>Mobile: +34 611.205.938
        <svg viewBox="0 0 10 10"><rect x="0" y="1.5" width="10" height="7"/></svg></li>
      <li>tommaso.ferlini@brivomatex.example
        <svg viewBox="0 0 10 10"><circle cx="5" cy="5" r="5"/></svg></li>
    </ul>
    <p class="tagline">Lantern for the Steady Growth</p>
  </section>
</body>
</html>
```